Creative Stationary for Solo Law Firm

I am looking for stationary designs for my solo law firm called TM Halvorsen Law PLLC. My logo is attached. I'd like the logo incorporated into the design.

I'm looking for a stationary design that is a bit outside of the box and not too standard or boring. The final design should communicate professionalism.

Target Market(s)

United States Clients, Opposing Counsel

Industry/Entity Type

Legal

Font styles to use
Sans Serif

Requirements
Must have
• The stationary design must incorporate my logo design attached. The design itself must be creative. The envelope design must follow standard United States designs with room for the postage stamp at the top right corner and space for the recipient's address in the middle.

```html
<!DOCTYPE html>
<html lang="en">
<head>
<meta charset="utf-8">
<title>TM Halvorsen Law – Stationery</title>
<link href="https://fonts.googleapis.com/css2?family=Marcellus+SC&family=Questrial&family=Great+Vibes&family=Arimo:wght@400;700&display=swap" rel="stylesheet">
<style>
:root{
  --navy:#1c2a6b;
  --paper:#f7f7f7;
  --ink:#333;
  --muted:#666;
  --rule:#c9c9c9;
  --bg:#d3d3d7;
  --on-navy:#ffffff;
}
*{box-sizing:border-box;margin:0;padding:0}
html,body{width:1200px;height:1068px;overflow:hidden;background:var(--bg)}
body{position:relative;font-family:"Questrial",sans-serif;color:var(--ink)}
.piece{position:absolute;background:var(--paper)}
.navy{background:var(--navy);color:var(--on-navy)}
.brand{font-family:"Marcellus SC",serif;letter-spacing:.3px;color:var(--navy);white-space:nowrap;position:absolute}
.navy .brand,.folder-panel .brand,.flap .brand{color:var(--on-navy)}
.foot{position:absolute;font-size:4.4px;line-height:6px;color:var(--muted)}
.foot b{color:var(--navy)}
.web{position:absolute;font-size:4.4px;color:var(--muted)}
.web b{color:var(--navy)}
.rule{position:absolute;height:1px;background:var(--rule)}

/* folder */
.folder{left:67px;top:74px;width:687px;height:458px;background:transparent}
.folder-panel{position:absolute;top:0;width:343px;height:458px;background:var(--navy);border-radius:4px}
.folder-panel.back{left:0}
.folder-panel.front{left:344px}
.folder .foot{color:#c9cde0}
.folder .foot b{color:var(--on-navy)}

/* envelope */
.envelope{left:802px;top:42px;width:332px;height:212px}
.envelope .flap{position:absolute;left:0;top:0;width:332px;height:46px;background:var(--navy)}
.envelope .flap .brand{transform:rotate(180deg);font-size:8px;left:126px;top:18px}

/* compliments slip */
.slip{left:802px;top:282px;width:316px;height:150px}
.slip .script{position:absolute;font-family:"Great Vibes",cursive;color:var(--navy);font-size:14px;left:21px;top:99px}

/* cards */
.card{top:470px;width:128px;height:70px;overflow:hidden}
.card-front{left:802px}
.card-back{left:964px}
.card-front .brand{font-size:6.3px;right:7px;top:15px}
.card-back .brand{font-size:9px;left:0;width:100%;text-align:center;top:30px}
.card .name{position:absolute;left:8px;top:14px;font-family:"Arimo",sans-serif;font-weight:700;font-size:4.1px;color:var(--navy)}
.card .role{position:absolute;left:8px;top:19px;font-size:3.6px;color:var(--muted)}
.card .contact{position:absolute;left:8px;top:51px;font-size:3.4px;line-height:4.4px;color:var(--muted)}
.card .addr{position:absolute;right:9px;top:51px;font-size:3.4px;line-height:4.4px;color:var(--muted);text-align:right}

/* letterhead & fax & blank */
.sheet{top:578px;width:316px;height:446px}
.letter{left:66px}
.fax{left:434px}
.blank{left:802px}
.blank .brand{font-size:7.5px;right:18px;top:21px}
.letter-body{position:absolute;left:28px;top:104px;width:258px;font-size:4.6px;line-height:5.8px;color:#444}
.letter-body p{margin-bottom:5px;text-align:justify}
.letter-body .salute{font-family:"Arimo",sans-serif;font-weight:700}
.sign-off{position:absolute;left:28px;top:300px;font-size:4.6px;line-height:5.8px;color:#444}
.signature{position:absolute;left:66px;top:293px;width:56px;height:32px;background:linear-gradient(90deg,rgba(80,90,190,.15),rgba(80,90,190,.05));border-radius:3px}

.fax-title{position:absolute;right:30px;top:22px;font-family:"Arimo",sans-serif;font-size:32px;color:#1a1a1a}
.fax-table{position:absolute;left:28px;top:74px;width:258px;border-collapse:collapse;font-family:"Arimo",sans-serif;font-size:4.3px}
.fax-table td{border:1px solid #999;height:9.5px;padding:0 3px;color:#333}
.fax-table .lab{width:27px;font-weight:700}
.fax-checks{position:absolute;left:28px;top:130px;width:258px;height:10px;display:flex;border:1px solid #999;background:#ececec;font-family:"Arimo",sans-serif;font-size:4px;font-weight:700}
.fax-checks span{flex:1;text-align:center;line-height:8px;border-right:1px solid #999}
.fax-checks span:last-child{border-right:none}
.fax-comments{position:absolute;left:28px;top:139px;width:258px;height:263px;border:1px solid #999;font-family:"Arimo",sans-serif;font-size:4px;text-align:center;padding-top:5px}
</style>
</head>
<body>

<!-- presentation folder -->
<div class="piece folder">
  <div class="folder-panel back">
    <div class="foot" style="left:30px;top:421px">418 Alder Creek Road, Suite 200, Bellmont, Oregon<br><b>Tel:</b> 503.555.0148 · <b>Email:</b> info@tmhalvorsenlaw.com<br>www.<b>tmhalvorsenlaw</b>.com</div>
  </div>
  <div class="folder-panel front">
    <div class="brand" style="font-size:18px;left:92px;top:70px">TM Halvorsen Law</div>
  </div>
</div>

<!-- envelope -->
<div class="piece envelope">
  <div class="flap"><div class="brand">TM Halvorsen Law</div></div>
  <div class="brand" style="font-size:12px;left:19px;top:75px">TM Halvorsen Law</div>
  <div class="rule" style="left:19px;top:181px;width:296px"></div>
  <div class="foot" style="left:19px;top:186px">418 Alder Creek Road, Suite 200, Bellmont, Oregon<br><b>Tel:</b> 503.555.0148 · <b>Email:</b> info@tmhalvorsenlaw.com</div>
  <div class="web" style="right:18px;top:186px">www.<b>tmhalvorsenlaw</b>.com</div>
</div>

<!-- compliments slip -->
<div class="piece slip">
  <div class="brand" style="font-size:12px;left:21px;top:24px">TM Halvorsen Law</div>
  <div class="script">With Compliments</div>
  <div class="rule" style="left:21px;top:120px;width:274px"></div>
  <div class="foot" style="left:21px;top:125px">418 Alder Creek Road, Suite 200, Bellmont, Oregon<br><b>Tel:</b> 503.555.0148 · <b>Email:</b> info@tmhalvorsenlaw.com</div>
  <div class="web" style="right:21px;top:125px">www.<b>tmhalvorsenlaw</b>.com</div>
</div>

<!-- business cards -->
<div class="piece card card-front">
  <div class="name">JORDAN WHITLOCK</div>
  <div class="role">General Manager</div>
  <div class="brand">TM Halvorsen Law</div>
  <div class="contact">T 503.555.0148<br>E info@tmhalvorsenlaw.com<br>W www.tmhalvorsenlaw.com</div>
  <div class="addr">418 Alder Creek Road<br>Suite 200<br>Bellmont, Oregon</div>
</div>
<div class="piece card card-back navy">
  <div class="brand">TM Halvorsen Law</div>
</div>

<!-- letterhead -->
<div class="piece sheet letter">
  <div class="brand" style="font-size:13px;left:28px;top:35px">TM Halvorsen Law</div>
  <div class="letter-body">
    <p>30.02.2015</p>
    <p>Recipient's name<br>Maple Court 12<br>20455 Northfield<br>USA</p>
    <p class="salute" style="margin-top:22px">Dear sir,</p>
    <p>Thank you for your recent inquiry. We have reviewed the documents you provided and prepared a short summary of the next steps for your matter.</p>
    <p>Please find enclosed the agreement for your review. Kindly sign and return one copy at your earliest convenience so that we may proceed.</p>
    <p>Should you have any questions regarding the terms, our office is available to discuss them by phone or in person during regular hours.</p>
    <p>We appreciate the opportunity to assist you and look forward to working together.</p>
  </div>
  <div class="sign-off">Yours Sincerely,<br><b style="font-family:'Arimo',sans-serif">Elin Varga</b></div>
  <div class="signature" role="img" aria-label="Handwritten signature"></div>
  <div class="rule" style="left:28px;top:417px;width:258px"></div>
  <div class="foot" style="left:28px;top:421px">418 Alder Creek Road, Suite 200, Bellmont, Oregon<br><b>Tel:</b> 503.555.0148 · <b>Email:</b> info@tmhalvorsenlaw.com</div>
  <div class="web" style="right:30px;top:421px">www.<b>tmhalvorsenlaw</b>.com</div>
</div>

<!-- fax cover -->
<div class="piece sheet fax">
  <div class="brand" style="font-size:13px;left:28px;top:35px">TM Halvorsen Law</div>
  <div class="fax-title">FAX</div>
  <table class="fax-table">
    <tr><td class="lab">To:</td><td></td><td class="lab">From:</td><td></td></tr>
    <tr><td class="lab">Fax:</td><td></td><td class="lab">Pages:</td><td></td></tr>
    <tr><td class="lab">Phone:</td><td></td><td class="lab">Date:</td><td></td></tr>
    <tr><td class="lab">Re:</td><td></td><td class="lab">CC:</td><td></td></tr>
  </table>
  <div class="fax-checks"><span>☐ Urgent</span><span>☐ For Review</span><span>☐ Please Comment</span><span>☐ Please Reply</span><span>☐ Please Recycle</span></div>
  <div class="fax-comments">COMMENTS:</div>
  <div class="rule" style="left:28px;top:417px;width:258px"></div>
  <div class="foot" style="left:28px;top:421px">418 Alder Creek Road, Suite 200, Bellmont, Oregon<br><b>Tel:</b> 503.555.0148 · <b>Email:</b> info@tmhalvorsenlaw.com</div>
  <div class="web" style="right:30px;top:421px">www.<b>tmhalvorsenlaw</b>.com</div>
</div>

<!-- continuation sheet -->
<div class="piece sheet blank">
  <div class="brand">TM Halvorsen Law</div>
</div>

</body>
</html>
```